Mirela Hartsby ADHD coach needs a flyer

I need a flyer to be sent by email. the copy is attached. It can be changed/reduced to fit the flyer. I would like to keep my website colors. My website is www.mirelahartsby.example - Thank you!

```html
<!DOCTYPE html>
<html lang="en">
<head>
<meta charset="utf-8">
<title>Mirela Hartsby – ADHD Academic Success Coach</title>
<link href="https://fonts.googleapis.com/css2?family=Montserrat:ital,wght@0,200;0,300;0,400;0,500;0,700;0,800;1,400;1,500&display=swap" rel="stylesheet">
<style>
  :root {
    --sky: #9cb8c4;
    --slate: #7d8a89;
    --slate-soft: #9aa7a7;
    --photo-gray: #a3abab;
    --ink: #3f4446;
    --quote-ink: #6f8189;
    --paper: #f3f4f5;
    --pill-light: #eceeef;
    --footer: #575c5f;
    --white: #ffffff;
  }
  * { margin: 0; padding: 0; box-sizing: border-box; }
  html, body { width: 848px; height: 1200px; overflow: hidden; }
  body { font-family: "Montserrat", Arial, sans-serif; background: var(--paper); color: var(--ink); }
  .flyer { position: relative; width: 848px; height: 1200px; overflow: hidden;
    background: linear-gradient(#ffffff 560px, var(--paper) 1000px, #e9ebec 1114px); }
  .abs { position: absolute; }

  .hero { position: absolute; left: 0; top: 0; width: 848px; height: 558px; }
  .hero svg { display: block; }

  .title-light { left: 48px; top: 52px; font-size: 63px; font-weight: 200; color: var(--white); letter-spacing: 2px; line-height: 1; }
  .title-bold { left: 48px; top: 112px; font-size: 62px; font-weight: 800; color: var(--white); letter-spacing: 1px; line-height: 1; }
  .subtitle { left: 62px; top: 184px; font-size: 15.5px; font-weight: 400; color: var(--white); line-height: 20px; }

  .intro { left: 48px; color: var(--white); font-size: 10.6px; font-weight: 300; line-height: 13.6px; }
  .intro.p1 { top: 244px; width: 436px; }
  .intro.p2 { top: 285px; width: 420px; }
  .intro.p3 { top: 380px; width: 388px; text-align: justify; }

  .name-tab { left: 504px; top: 480px; width: 312px; height: 58px; background: var(--sky); border-radius: 8px 8px 0 0; color: var(--white); text-align: center; }
  .name-tab .name { font-size: 24.5px; font-weight: 500; letter-spacing: 0.5px; margin-top: 8px; line-height: 28px; }
  .name-tab .role { font-size: 12.6px; font-weight: 400; letter-spacing: 0.5px; line-height: 16px; }

  .testimonial-card { left: 514px; top: 538px; width: 292px; height: 456px; background: var(--white); box-shadow: 0 6px 14px rgba(0,0,0,0.08); }

  .results { left: 56px; top: 598px; width: 440px; font-size: 16.4px; font-style: italic; font-weight: 500; color: var(--quote-ink); line-height: 20px; }

  .helps-band { left: 50px; top: 696px; width: 442px; height: 47px; background: var(--slate); color: var(--white); font-size: 38px; font-weight: 300; line-height: 47px; padding-left: 24px; box-shadow: 0 6px 10px rgba(0,0,0,0.12); }
  .helps-band b { font-weight: 800; }

  .benefit { width: 200px; font-size: 11.4px; font-weight: 400; line-height: 15.4px; color: var(--ink); }
  .benefit .chev { position: absolute; left: -23px; top: -1px; }

  .say-mark { font-size: 92px; font-weight: 800; color: var(--slate-soft); line-height: 1; font-family: "Montserrat", Georgia, serif; }
  .say-head { font-size: 25px; font-weight: 300; color: var(--ink); line-height: 27px; }
  .say-head b { font-weight: 500; }
  .say-text { left: 540px; width: 242px; font-size: 10.6px; line-height: 12.8px; color: var(--ink); text-align: justify; font-weight: 400; }

  .pill { top: 1016px; height: 68px; border-radius: 50%; display: flex; align-items: center; justify-content: center; text-align: center; font-size: 11.4px; line-height: 15.4px; box-shadow: 0 8px 10px -6px rgba(0,0,0,0.15); }
  .pill.lead { background: var(--slate); color: var(--white); font-size: 19.5px; font-weight: 800; line-height: 23px; }
  .pill.light { background: var(--pill-light); color: var(--ink); }
  .pill.sky { background: var(--sky); color: var(--white); }
  .pill.soft { background: var(--slate-soft); color: var(--white); }

  .footer { left: 0; top: 1114px; width: 848px; height: 86px; background: var(--footer); color: var(--white); }
  .footer .ask { position: absolute; left: 49px; top: 24px; font-size: 17px; font-weight: 300; letter-spacing: 1.4px; line-height: 20px; }
  .footer .contact { position: absolute; left: 444px; top: 24px; font-size: 17px; font-weight: 700; letter-spacing: 1.2px; line-height: 20px; }
  .footer .chev { position: absolute; left: 398px; top: 35px; }
</style>
</head>
<body>
<main class="flyer">

  <div class="hero">
    <svg width="848" height="558" viewBox="0 0 848 558">
      <rect x="0" y="0" width="848" height="558" fill="var(--sky)"/>
      <defs>
        <linearGradient id="portraitTone" x1="0" y1="0" x2="0" y2="1">
          <stop offset="0" stop-color="#a7aeae"/>
          <stop offset="0.45" stop-color="#b8b0b0"/>
          <stop offset="1" stop-color="#d9c4c6"/>
        </linearGradient>
      </defs>
      <polygon points="576,0 848,0 848,558 416,558" fill="var(--photo-gray)"/>
      <polygon points="500,60 848,60 848,558 470,558" fill="url(#portraitTone)" opacity="0.55"
        role="img" aria-label="Portrait photo of the coach with arms crossed, wearing a light pink blazer"/>
    </svg>
  </div>

  <div class="abs title-light">HELPING</div>
  <div class="abs title-bold">YOUR CHILD</div>

  <svg class="abs" style="left:48px;top:181px" width="450" height="48" viewBox="0 0 450 48">
    <polygon points="0,0 450,0 436,48 0,48" fill="var(--slate)"/>
  </svg>
  <div class="abs subtitle">with ADHD or Other Learning<br>Challenges Thrive in College and Beyond</div>

  <p class="abs intro p1">Academic success coaching that leads to lifelong transformation for students with ADHD and similar challenges that may have impeded their ability to thrive.</p>
  <p class="abs intro p2">Sending your child off to college can feel scary, especially if that college is hundreds of miles away. You worry about how they’ll do on their own—whether they’ll make friends, earn good grades, and be happy—especially without you there to support them daily. You know your child is bright, and you want them to have a great future, but you’re concerned they will struggle without the right support and resources.</p>
  <p class="abs intro p3">You don’t need to feel helpless as you send your child off to this next stage of their lives. Mirela is dedicated to making that transition easier for everyone. Mirela Hartsby has years of experience helping students thrive despite their challenges. She sees your child’s potential and helps them see it, too. She provides a safety net as they adjust to a new environment at college. Her services are comprehensive and adaptable, based on the requirements of each individual: helping with course selection and scheduling, time management, study strategies, focus, making new friends, and adapting to change. Through it all, Mirela guides students through fundamental work on mindset to ensure that changes stick.</p>

  <div class="abs name-tab">
    <div class="name">MIRELA HARTSBY, Ph.D.</div>
    <div class="role">ADHD Academic Success Coach</div>
  </div>

  <div class="abs testimonial-card"></div>

  <p class="abs results">Mirela has taken students from failing to a 3.0 GPA, and from a C student to the Dean’s List, in just one semester. It doesn’t take years to provide lasting results; all it takes is the right guide.</p>

  <div class="abs helps-band">HOW <b>MIRELA</b> HELPS</div>

  <div class="abs benefit" style="left:74px;top:770px">
    <svg class="chev" width="16" height="14" viewBox="0 0 16 14"><path d="M1 1l6 6-6 6M8 1l6 6-6 6" fill="none" stroke="var(--slate-soft)" stroke-width="1.2"/></svg>
    Tailors support so that your child improves focus and maximizes their potential in college and beyond.
  </div>
  <div class="abs benefit" style="left:74px;top:848px">
    <svg class="chev" width="16" height="14" viewBox="0 0 16 14"><path d="M1 1l6 6-6 6M8 1l6 6-6 6" fill="none" stroke="var(--slate-soft)" stroke-width="1.2"/></svg>
    Helps with the logistics of scheduling in a way that most advisors can’t, enrolling students in the courses that best suit their learning style.
  </div>
  <div class="abs benefit" style="left:74px;top:940px">
    <svg class="chev" width="16" height="14" viewBox="0 0 16 14"><path d="M1 1l6 6-6 6M8 1l6 6-6 6" fill="none" stroke="var(--slate-soft)" stroke-width="1.2"/></svg>
    Nurtures the brilliance in your bright child.
  </div>
  <div class="abs benefit" style="left:305px;top:770px">
    <svg class="chev" width="16" height="14" viewBox="0 0 16 14"><path d="M1 1l6 6-6 6M8 1l6 6-6 6" fill="none" stroke="var(--slate-soft)" stroke-width="1.2"/></svg>
    Understands your child’s unique needs - she sees the gifts that others often miss.
  </div>
  <div class="abs benefit" style="left:305px;top:848px">
    <svg class="chev" width="16" height="14" viewBox="0 0 16 14"><path d="M1 1l6 6-6 6M8 1l6 6-6 6" fill="none" stroke="var(--slate-soft)" stroke-width="1.2"/></svg>
    Knows the academic landscape intimately, including the challenges faced by students with ADHD and other conditions.
  </div>
  <div class="abs benefit" style="left:305px;top:940px">
    <svg class="chev" width="16" height="14" viewBox="0 0 16 14"><path d="M1 1l6 6-6 6M8 1l6 6-6 6" fill="none" stroke="var(--slate-soft)" stroke-width="1.2"/></svg>
    Provides a balance between encouraging students and challenging them.
  </div>

  <div class="abs say-mark" style="left:536px;top:556px">“</div>
  <div class="abs say-head" style="left:616px;top:561px">What<br><b>Parents</b> Say</div>
  <p class="abs say-text" style="top:632px">“Mirela was the glue that kept our daughter in college… as our daughter’s Academic Coach, [she] gave our daughter the ability to finish strong by empowering her with the skills needed to be successful.”—Renata</p>
  <p class="abs say-text" style="top:708px">“Mirela has always told my daughter not that she can succeed, but that she will succeed.”—Lorna</p>

  <div class="abs say-mark" style="left:536px;top:765px">“</div>
  <div class="abs say-head" style="left:614px;top:770px">What<br><b>Students</b> Say</div>
  <p class="abs say-text" style="top:842px">Last semester I completed all 16 hours and I had the highest GPA I’ve ever had!” —Former student</p>
  <p class="abs say-text" style="top:894px">“Under her instruction, my grades began to improve. I ended up making the Dean’s List during my time at Ridgefield, and I was also inducted into Sigma Theta Vale. I am currently in my first year of law school at Northbrook University, a top tier school.”—Former student</p>

  <div class="abs pill lead" style="left:38px;width:156px">YOU<br>WILL HAVE:</div>
  <div class="abs pill light" style="left:197px;width:158px">Less stress, knowing<br>that your child is in<br>good hands.</div>
  <div class="abs pill sky" style="left:359px;width:158px">Fewer sleepless<br>nights worrying<br>about your child.</div>
  <div class="abs pill light" style="left:519px;width:158px">Confidence that<br>they are receiving<br>the right support.</div>
  <div class="abs pill soft" style="left:678px;width:132px">Joy and pride<br>at seeing them<br>do well.</div>

  <footer class="abs footer">
    <div class="ask">TO LEARN MORE AND DISCUSS<br>YOUR CHILD’S INDIVIDUAL NEEDS,</div>
    <svg class="chev" width="16" height="16" viewBox="0 0 16 16"><path d="M1 1l7 7-7 7M8 1l7 7-7 7" fill="none" stroke="var(--white)" stroke-width="1.2"/></svg>
    <div class="contact">CALL 555·013·4862 OR<br>EMAIL COACH@MIRELAHARTSBY.EXAMPLE</div>
  </footer>

</main>
</body>
</html>
```